Bookkeeping website design

We need a basic site design for wordpress.
We are a bookkeeping business and will need to present a look consistent with the colours and style of the logo.

Target Market(s)

Business owners

Industry/Entity Type

Accounting/Bookkeeping

Coding

Coded - Design and coding required

Number of Pages Required

1 page

```html
<!DOCTYPE html>
<html lang="en">
<head>
<meta charset="utf-8">
<title>Ledgerline Bookkeeping</title>
<link href="https://fonts.googleapis.com/css2?family=Nunito+Sans:wght@400;600;700;800&display=swap" rel="stylesheet">
<style>
:root{
  --green:#98cb30;
  --blue:#00c0f2;
  --ink:#0f2e36;
  --text:#2b2b2b;
  --muted:#666;
  --hero:#eef2f3;
  --soft:#f4f4f4;
  --footer:#0d2a32;
  --white:#fff;
}
*{box-sizing:border-box;margin:0;padding:0}
html,body{width:1200px;height:3817px;overflow:hidden}
body{font-family:"Nunito Sans",sans-serif;color:var(--text);background:var(--white);position:relative}
.abs{position:absolute}
.ph{position:absolute}
.btn{position:absolute;background:var(--blue);color:var(--white);font-weight:800;font-size:13px;letter-spacing:.3px;display:flex;align-items:center;justify-content:center;box-shadow:0 3px 8px rgba(0,0,0,.12)}
h2.section-title{position:absolute;left:0;width:1200px;text-align:center;font-size:30px;font-weight:800;color:var(--ink)}

/* header */
.site-header{position:absolute;left:0;top:0;width:1200px;height:640px;background:var(--hero)}
.brand{position:absolute;display:flex;align-items:center;gap:10px;font-weight:800;font-size:22px;color:var(--ink)}
.brand .dot{width:26px;height:26px;border-radius:50%;background:var(--green)}
.nav{position:absolute;top:22px;left:586px;display:flex;gap:38px;font-size:14px;color:var(--ink);font-weight:600}
.login{position:absolute;left:1028px;top:14px;width:98px;height:36px;background:var(--green);color:#fff;font-weight:800;font-size:13px;display:flex;align-items:center;justify-content:center;gap:6px}
.header-rule{position:absolute;left:71px;top:76px;width:1055px;height:1px;background:#dde3e5}
.hero-title{position:absolute;left:71px;top:222px;font-size:43px;line-height:53px;font-weight:800;color:var(--ink)}
.hero-text{position:absolute;left:71px;top:348px;width:560px;font-size:19px;line-height:31px;color:#222}

/* about */
.about-panel{position:absolute;left:600px;top:680px;width:526px;height:344px;background:var(--green);color:#fff}
.about-panel h3{position:absolute;left:86px;top:70px;font-size:29px;font-weight:800}
.about-panel p{position:absolute;left:86px;top:118px;width:370px;font-size:14px;line-height:22px}

/* services */
.services{position:absolute;left:0;top:1062px;width:1200px;height:454px;background:var(--soft)}
.service-card{position:absolute;top:1164px;width:338px;height:271px;background:#e9e9e9;text-align:center}
.service-card .photo{position:absolute;left:0;top:0;width:100%;height:89px;background:linear-gradient(135deg,#6f7478,#b9bec2)}
.service-card .icon{position:absolute;left:126px;top:26px;width:86px;height:86px;border-radius:50%;background:var(--green);border:4px solid #fff;display:flex;align-items:center;justify-content:center}
.service-card h4{position:absolute;left:0;width:100%;top:128px;font-size:20px;font-weight:800;color:#222}
.service-card p{position:absolute;left:30px;width:278px;top:163px;font-size:14px;line-height:22px;color:#555}
.service-card .plus{position:absolute;left:0;width:100%;top:228px;color:var(--blue);font-weight:800;font-size:18px}
.arrow{position:absolute;top:1270px}

/* process */
.process{position:absolute;left:0;top:1516px;width:1200px;height:392px;background:var(--blue)}
.process h3{position:absolute;left:500px;top:30px;font-size:29px;font-weight:800;color:var(--ink)}
.step-card{position:absolute;top:100px;width:198px;height:249px;background:#fff;clip-path:polygon(0 0,78% 0,100% 22%,100% 100%,0 100%)}
.step-card .photo{position:absolute;left:6px;top:6px;width:186px;height:120px;clip-path:polygon(0 0,74% 0,100% 60%,0 100%);background:linear-gradient(135deg,#4a6077,#c6d0d8)}
.step-card .label{position:absolute;right:10px;top:98px;text-align:right;color:#111;font-weight:800;line-height:1}
.step-card .label small{display:block;font-size:13px}
.step-card .label b{font-size:34px}
.step-card p{position:absolute;left:10px;top:180px;width:175px;font-size:14px;line-height:20px;color:#222}

/* testimonials */
.testimonials{position:absolute;left:0;top:1908px;width:1200px;height:443px;background:var(--soft)}
.quote-card{position:absolute;top:2024px;width:338px;height:188px;background:#fff;border:1px solid #e3e3e3}
.quote-card::after{content:"";position:absolute;left:40px;bottom:-14px;border-left:14px solid transparent;border-right:14px solid transparent;border-top:14px solid #fff}
.stars{position:absolute;left:24px;top:18px;color:#f3c01b;font-size:14px;letter-spacing:1px}
.qmark{position:absolute;font-size:30px;font-weight:800;color:#333;line-height:1}
.quote-card p{position:absolute;left:24px;top:64px;width:292px;font-size:14.5px;line-height:22.5px;color:#333}
.person{position:absolute;top:2232px;display:flex;align-items:center;gap:14px}
.avatar{width:58px;height:58px;border-radius:50%;background:linear-gradient(135deg,#2c2c2c,#7a7a7a)}
.person strong{display:block;font-size:16px;font-weight:600;color:#111}
.person span{font-size:12.5px;color:var(--blue)}

/* blog */
.featured{position:absolute;left:71px;top:2467px;width:539px;height:373px;background:linear-gradient(120deg,#1f1b19,#4a4542 60%,#6d6a68);color:#fff;box-shadow:0 4px 10px rgba(0,0,0,.2)}
.featured .tag{position:absolute;left:44px;top:44px;padding-left:10px;border-left:3px solid var(--blue);font-size:15px}
.featured h3{position:absolute;left:44px;top:94px;width:470px;font-size:22.5px;line-height:31px;font-weight:600}
.featured p{position:absolute;left:44px;top:210px;width:470px;font-size:13.5px;line-height:21px}
.post{position:absolute;left:650px;width:476px;height:114px;background:#fff;border:1px solid #ddd;box-shadow:0 2px 6px rgba(0,0,0,.08)}
.post .thumb{position:absolute;left:12px;top:15px;width:88px;height:84px;background:linear-gradient(135deg,#8a9aa6,#dfe5e8)}
.post p{position:absolute;left:150px;top:22px;width:310px;font-size:14.5px;line-height:21px;color:#333}
.post .date{position:absolute;left:150px;top:72px;font-size:12px;font-weight:700;color:#777;display:flex;align-items:center;gap:6px}

/* call to action */
.cta-band{position:absolute;left:0;top:2900px;width:1200px;height:466px}
.cta-title{position:absolute;left:64px;top:3034px;font-size:35px;font-weight:800;color:var(--ink)}
.cta-text{position:absolute;left:71px;top:3096px;width:460px;font-size:19px;line-height:26px;color:#1a1a1a}
.field{position:absolute;top:3200px;height:40px;background:#fff;font-size:13px;color:#333;padding-left:12px;display:flex;align-items:center}

/* footer */
.site-footer{position:absolute;left:0;top:3366px;width:1200px;height:451px;background:var(--footer);color:#fff}
.site-footer h5{position:absolute;top:96px;font-size:16.5px;font-weight:600}
.site-footer ul{position:absolute;top:150px;list-style:none;font-size:14px;line-height:18px}
.site-footer li{margin-bottom:12px}
.bullets li{padding-left:23px;position:relative}
.bullets li::before{content:"";position:absolute;left:0;top:5px;width:7px;height:7px;border-radius:50%;background:var(--green)}
.contact{position:absolute;left:71px;display:flex;align-items:flex-start;gap:14px;font-size:14px;line-height:19px}
.contact .ic{width:22px;height:22px;border-radius:50%;background:var(--blue);flex:none}
.newsletter-text{position:absolute;left:881px;top:148px;width:245px;font-size:14px;line-height:22px}
.newsletter-input{position:absolute;left:883px;top:247px;width:243px;height:40px;background:#fff;color:#333;font-size:13px;display:flex;align-items:center;padding-left:14px}
.copyright{position:absolute;left:0;width:1200px;top:389px;text-align:center;font-size:13px}
.copyright span{color:var(--green)}
</style>
</head>
<body>

<header class="site-header">
  <div class="brand" style="left:71px;top:24px"><span class="dot"></span>Ledgerline</div>
  <nav class="nav"><span>Home</span><span>About</span><span>Services</span><span>Resources</span><span>Contact</span></nav>
  <div class="login">
    <svg width="11" height="12" viewBox="0 0 11 12"><rect x="1" y="5" width="9" height="7" fill="#fff"/><path d="M3 5V3.5a2.5 2.5 0 0 1 5 0V5" stroke="#fff" stroke-width="1.6" fill="none"/></svg>
    LOG IN
  </div>
  <div class="header-rule"></div>
  <div class="ph" role="img" aria-label="Hands typing on a laptop showing a bookkeeping page beside a calculator" style="left:474px;top:89px;width:726px;height:551px;background:linear-gradient(160deg,#dfe4e6,#b9c0c4 55%,#e6d6cc);clip-path:polygon(45% 0,100% 0,100% 100%,0 100%,0 55%)"></div>
  <h1 class="hero-title">You Run Your Business.<br>We’ll Handle Your Finances.</h1>
  <p class="hero-text">Many desktop publishing packages and web page editors now use Lorem Ipsum as their default model text,</p>
  <div class="btn" style="left:71px;top:434px;width:159px;height:45px">START A FREE TRIAL</div>
</header>

<section class="about">
  <div class="ph" role="img" aria-label="Businessman in a suit reviewing documents at a desk" style="left:71px;top:680px;width:529px;height:344px;background:linear-gradient(135deg,#d9dde0,#8e969c 60%,#5b6268)"></div>
  <div class="about-panel">
    <h3>About Us</h3>
    <p>Many desktop publishing packages and web page editors now use Lorem Ipsum as their default model text,and a search for ‘lorem ipsum’ will uncover many web sites still in their infancy.</p>
    <div class="btn" style="left:86px;top:230px;width:111px;height:36px">READ MORE</div>
  </div>
</section>

<section class="services">
  <h2 class="section-title" style="top:42px">Our Services</h2>
</section>
<svg class="arrow" style="left:44px" width="14" height="22" viewBox="0 0 14 22"><path d="M11 2 3 11l8 9" stroke="#888" stroke-width="2.5" fill="none"/></svg>
<svg class="arrow" style="left:1137px" width="14" height="22" viewBox="0 0 14 22"><path d="M3 2l8 9-8 9" stroke="#222" stroke-width="2.5" fill="none"/></svg>

<article class="service-card" style="left:71px">
  <div class="photo" role="img" aria-label="Office desk with papers"></div>
  <div class="icon"><svg width="40" height="38" viewBox="0 0 40 38" fill="none" stroke="#1d2b1a" stroke-width="2"><rect x="3" y="4" width="26" height="30"/><path d="M8 11h16M8 17h16M8 23h10"/><rect x="22" y="18" width="15" height="18"/><path d="M25 22h9M25 27h9M25 32h9"/></svg></div>
  <h4>Bookkeeping</h4>
  <p>Many desktop publishing packages and web page editors now use Lorem Ipsum as their default.</p>
  <div class="plus">+</div>
</article>
<article class="service-card" style="left:431px">
  <div class="photo" role="img" aria-label="Payroll paperwork on a desk"></div>
  <div class="icon"><svg width="40" height="38" viewBox="0 0 40 38" fill="none" stroke="#1d2b1a" stroke-width="2"><rect x="4" y="20" width="32" height="14"/><circle cx="20" cy="27" r="4"/><path d="M6 16l10-8 6 5 12-9M28 4h6v6"/></svg></div>
  <h4>Payroll</h4>
  <p>Many desktop publishing packages and web page editors now use Lorem Ipsum as their default.</p>
  <div class="plus">+</div>
</article>
<article class="service-card" style="left:791px">
  <div class="photo" role="img" aria-label="Laptop and tax forms on a desk"></div>
  <div class="icon"><svg width="40" height="38" viewBox="0 0 40 38" fill="none" stroke="#1d2b1a" stroke-width="2"><rect x="6" y="3" width="26" height="32"/><text x="10" y="14" font-size="9" font-family="sans-serif" fill="#1d2b1a" stroke="none">TAX</text><path d="M10 20h18M10 25h18M10 30h12"/></svg></div>
  <h4>Tax</h4>
  <p>Many desktop publishing packages and web page editors now use Lorem Ipsum as their default.</p>
  <div class="plus">+</div>
</article>
<div class="btn" style="left:545px;top:1455px;width:110px;height:38px">VIEW ALL</div>

<section class="process">
  <div class="ph" role="img" aria-label="Hands holding a tablet showing bar charts" style="left:0;top:0;width:437px;height:392px;background:linear-gradient(135deg,#e3e8ec,#8d9aa3 55%,#3f4b53)"></div>
  <h3>Our Process</h3>
  <div class="step-card" style="left:505px">
    <div class="photo" role="img" aria-label="Person reviewing financial charts"></div>
    <div class="label"><small>STEP</small><b>01</b></div>
    <p>There are many variations of passages of Lorem Ipsum .</p>
  </div>
  <div class="step-card" style="left:712px">
    <div class="photo" role="img" aria-label="Hand writing with a pen on documents"></div>
    <div class="label"><small>STEP</small><b>02</b></div>
    <p>There are many variations of passages of Lorem Ipsum .</p>
  </div>
  <div class="step-card" style="left:924px">
    <div class="photo" role="img" aria-label="Stacks of coins"></div>
    <div class="label"><small>STEP</small><b>03</b></div>
    <p>There are many variations of passages of Lorem Ipsum .</p>
  </div>
</section>

<section class="testimonials">
  <h2 class="section-title" style="top:54px">Client Testimonial</h2>
</section>
<div class="quote-card" style="left:71px"><div class="stars">★★★★★</div><div class="qmark" style="left:24px;top:40px">“</div><p>There are many variations of passages of Lorem Ipsum available, but the majority have suffered alteration in some form, by injected humour,</p><div class="qmark" style="left:146px;top:136px">”</div></div>
<div class="quote-card" style="left:431px"><div class="stars">★★★★★</div><div class="qmark" style="left:24px;top:40px">“</div><p>There are many variations of passages of Lorem Ipsum available, but the majority have suffered alteration in some form, by injected humour,</p><div class="qmark" style="left:146px;top:136px">”</div></div>
<div class="quote-card" style="left:791px"><div class="stars">★★★★★</div><div class="qmark" style="left:24px;top:40px">“</div><p>There are many variations of passages of Lorem Ipsum available, but the majority have suffered alteration in some form, by injected humour,</p><div class="qmark" style="left:146px;top:136px">”</div></div>
<div class="person" style="left:119px"><div class="avatar" role="img" aria-label="Client portrait"></div><div><strong>Mara Ellison</strong><span>CEO at loremipsum</span></div></div>
<div class="person" style="left:479px"><div class="avatar" role="img" aria-label="Client portrait"></div><div><strong>Theo Brandt</strong><span>Businessman</span></div></div>
<div class="person" style="left:839px"><div class="avatar" role="img" aria-label="Client portrait"></div><div><strong>Mara Ellison</strong><span>CEO at loremipsum</span></div></div>

<section class="blog">
  <h2 class="section-title" style="top:2398px">Blog</h2>
  <article class="featured" role="img" aria-label="Featured post over a photo of a laptop keyboard">
    <div class="tag">Featured Post</div>
    <h3>Contrary to popular belief, Lorem Ipsum is not simply random text. It has roots in a piece of classical Latin literature from 45 BC,</h3>
    <p>Many desktop publishing packages and web page editors now use Lorem Ipsum as their default model text,and a search for ‘lorem ipsum’ will uncover many web sites still in their infancy.</p>
    <div class="btn" style="left:44px;top:286px;width:111px;height:36px">READ MORE</div>
  </article>
  <article class="post" style="top:2467px"><div class="thumb" role="img" aria-label="Laptop on a desk"></div><p>Many desktop publishing packages and web page editors</p><div class="date"><svg width="13" height="13" viewBox="0 0 13 13"><circle cx="6.5" cy="6.5" r="5.5" stroke="#888" fill="none"/><path d="M6.5 3.5v3h2.5" stroke="#888" fill="none"/></svg>20 OCT , 2021</div></article>
  <article class="post" style="top:2597px"><div class="thumb" role="img" aria-label="Plant growing from a jar of coins"></div><p>Many desktop publishing packages and web page editors</p><div class="date"><svg width="13" height="13" viewBox="0 0 13 13"><circle cx="6.5" cy="6.5" r="5.5" stroke="#888" fill="none"/><path d="M6.5 3.5v3h2.5" stroke="#888" fill="none"/></svg>20 OCT , 2021</div></article>
  <article class="post" style="top:2726px"><div class="thumb" role="img" aria-label="Person working at a laptop"></div><p>Many desktop publishing packages and web page editors</p><div class="date"><svg width="13" height="13" viewBox="0 0 13 13"><circle cx="6.5" cy="6.5" r="5.5" stroke="#888" fill="none"/><path d="M6.5 3.5v3h2.5" stroke="#888" fill="none"/></svg>20 OCT , 2021</div></article>
</section>

<section class="cta">
  <svg class="cta-band" width="1200" height="466" viewBox="0 0 1200 466"><polygon points="0,12 1200,62 1200,466 0,466" fill="var(--green)"/></svg>
  <div class="ph" role="img" aria-label="Hand pointing at analytics charts on a screen with a person writing notes" style="left:588px;top:2899px;width:538px;height:389px;background:linear-gradient(150deg,#f1f3f5,#b8c6d2 55%,#e8ded6)"></div>
  <h2 class="cta-title">Take Your First Step</h2>
  <p class="cta-text">Try us for free—we’ll do one prior month of your bookkeeping and prepare a set of financial statements for you to keep.</p>
  <div class="field" style="left:71px;width:160px">Full Name</div>
  <div class="field" style="left:240px;width:160px">Email</div>
  <div class="btn" style="left:409px;top:3200px;width:159px;height:40px">START A FREE TRIAL</div>
</section>

<footer class="site-footer">
  <div class="brand" style="left:71px;top:88px;color:#fff"><span class="dot"></span>Ledgerline</div>
  <div class="contact" style="top:182px"><span class="ic"></span><span>18 Harbor Lane Springfield<br>United States of America</span></div>
  <div class="contact" style="top:234px"><span class="ic"></span><span>555-014-2290</span></div>
  <div class="contact" style="top:279px"><span class="ic"></span><span>hello@ledgerline.example</span></div>

  <h5 style="left:333px">Quick Link</h5>
  <ul style="left:333px"><li>Home</li><li>About</li><li>Services</li><li>Resources</li><li>Contact</li></ul>

  <h5 style="left:481px">Services</h5>
  <ul class="bullets" style="left:481px;width:190px"><li>Bookkeeping</li><li>Payroll</li><li>Tax</li><li>Bill Pay</li><li>Financial Plannning &amp; Investment</li></ul>

  <h5 style="left:693px">Resources</h5>
  <ul class="bullets" style="left:693px"><li>Partner Program</li><li>Payment Method</li><li>Blog</li><li>FAQ</li><li>Guides &amp; Tools</li></ul>

  <h5 style="left:881px">Newsletter Subscribe</h5>
  <p class="newsletter-text">Get the latest in tax and small business updates and issues that affect your finances</p>
  <div class="newsletter-input">Enter Your Mail ID
    <svg style="position:absolute;right:14px;top:12px" width="18" height="16" viewBox="0 0 18 16"><path d="M1 8 17 1 12 15 9 9z" fill="var(--green)"/></svg>
  </div>
  <p class="copyright">© Copyright <span>ledgerlinebooks</span> 2021 . All rights reserved.</p>
</footer>

</body>
</html>
```